Yard Sign Design for luxury design & build company

Looking to have 18" x 24" company yard signs designed.
An update to the business logo might be helpful.
Photos are not necessary but use if you can make inspiring.

Industry: Construction

Looking for a large headline of "Basement Finishing"
Website: www.tamberlyhomes.com
Phone Number (612) 555-0174
FB link: facebook.com/tamberlyhomesmn
Instagram: www.instagram.com/tamberlyhomesmn

Industry/Entity Type

Construction

Colors

Designer to choose colors to be used in the design.

Requirements
Must have
• Impactful high end characteristics
Nice to have
• Depth and detail graphis

```html
<!DOCTYPE html>
<html lang="en">
<head>
<meta charset="utf-8">
<title>Basement Finishing Yard Sign</title>
<link rel="stylesheet" href="https://fonts.googleapis.com/css2?family=Bodoni+Moda:wght@400&family=Great+Vibes&family=Montserrat:wght@500;800&display=swap">
<style>
  :root {
    --red: #d42a25;
    --red-light: #e2372f;
    --charcoal: #47464a;
    --charcoal-dark: #3a393d;
    --white: #ffffff;
    --navy: #27306b;
    --ig-start: #8a2a8f;
    --ig-end: #f39a2b;
    --page: #e9e9ec;
  }
  * { margin: 0; padding: 0; box-sizing: border-box; }
  html, body { width: 1200px; height: 1038px; overflow: hidden; background: var(--page); }
  .sign {
    position: absolute; left: 232px; top: 29px;
    width: 735px; height: 980px;
    background: var(--white);
    overflow: hidden;
    box-shadow: 0 6px 24px rgba(0,0,0,.18);
  }
  .sign__header {
    position: absolute; left: 0; top: 0; width: 735px; height: 353px;
    background: var(--red);
    overflow: hidden;
  }
  .sign__header-arc {
    position: absolute; left: 250px; top: -360px;
    width: 760px; height: 760px; border-radius: 50%;
    background: var(--red-light);
  }
  .sign__website {
    position: absolute; left: 173px; width: 410px; top: 36px;
    text-align: center; white-space: nowrap;
    font-family: "Montserrat", sans-serif; font-weight: 500;
    font-size: 16px; letter-spacing: 7px; color: var(--white);
  }
  .sign__headline-main {
    position: absolute; left: 60px; top: 86px;
    font-family: "Bodoni Moda", serif; font-weight: 400;
    font-size: 108px; line-height: 1; color: var(--white);
    letter-spacing: -1px;
  }
  .sign__headline-script {
    position: absolute; left: 118px; top: 190px; z-index: 2;
    font-family: "Great Vibes", cursive;
    font-size: 168px; line-height: 1; color: var(--white);
    white-space: nowrap;
  }
  .sign__photo {
    position: absolute; left: 0; top: 353px; width: 735px; height: 438px;
    background: linear-gradient(180deg, #cfc9c2 0%, #a99a8a 45%, #6f5f50 100%);
  }
  .sign__photo-arc { position: absolute; left: 0; top: 353px; width: 735px; height: 60px; }
  .sign__brand {
    position: absolute; left: 550px; top: 632px; width: 159px; height: 159px;
    background: var(--white);
    display: flex; align-items: center; justify-content: center;
  }
  .sign__brand-name {
    font-family: "Montserrat", sans-serif; font-weight: 800;
    font-size: 17px; line-height: 1.2; letter-spacing: 1px;
    color: var(--charcoal-dark); text-align: center;
  }
  .sign__phone-band {
    position: absolute; left: 0; top: 791px; width: 735px; height: 120px;
    background: var(--charcoal);
  }
  .sign__phone {
    position: absolute; left: 0; width: 735px; top: 14px;
    text-align: center; white-space: nowrap;
    font-family: "Montserrat", sans-serif; font-weight: 800;
    font-size: 76px; letter-spacing: 7px; color: var(--white);
  }
  .sign__phone-rule { position: absolute; left: 0; top: 106px; width: 735px; height: 8px; }
  .sign__social {
    position: absolute; top: 931px; height: 27px; width: 278px;
    border-radius: 14px;
    display: flex; align-items: center; padding-left: 16px; gap: 14px;
    font-family: "Montserrat", sans-serif; font-weight: 500;
    font-size: 15px; letter-spacing: 3.5px; color: var(--white);
  }
  .sign__social--facebook { left: 67px; background: var(--navy); }
  .sign__social--instagram { left: 395px; background: linear-gradient(90deg, var(--ig-start), #c8327a 55%, var(--ig-end)); }
  .sign__social-dot { width: 10px; height: 10px; border-radius: 50%; background: var(--white); flex: none; }
</style>
</head>
<body>
  <div class="sign">
    <div class="sign__photo" role="img" aria-label="Photo of a finished basement with a pool table, bar, stone fireplace and wood floors"></div>
    <svg class="sign__photo-arc" viewBox="0 0 735 60" aria-hidden="true">
      <path d="M0 0 H735 V0 Q560 60 330 52 Q140 44 0 0 Z" fill="#3f3e42"/>
    </svg>

    <div class="sign__header">
      <div class="sign__header-arc"></div>
      <p class="sign__website">www.tamberlyhomes.com</p>
      <h1 class="sign__headline-main">Basement</h1>
    </div>
    <p class="sign__headline-script">Finishing</p>

    <div class="sign__brand">
      <span class="sign__brand-name">TAMBERLY<br>HOMES</span>
    </div>

    <div class="sign__phone-band">
      <p class="sign__phone">(612) 555-0174</p>
      <svg class="sign__phone-rule" viewBox="0 0 735 8" preserveAspectRatio="none" aria-hidden="true">
        <path d="M0 1 H695 L690 7 H0 Z" fill="var(--red)"/>
      </svg>
    </div>

    <div class="sign__social sign__social--facebook"><span class="sign__social-dot"></span>tamberlyhomesmn</div>
    <div class="sign__social sign__social--instagram"><span class="sign__social-dot"></span>tamberlyhomesmn</div>
  </div>
</body>
</html>
```